Business Card Design for a Lending Business (Hard Money loans)

We need a business card for our Real Estate Lending business. We do hard Money loans for real estate investors. We have an existing logo we like, see attached. I'd like the business card to mostly include the logo colors, but a bright color pop of some sort would be nice to see also. Card should include Logo, Company Name, Company Address, Employee Name, Cell Phone, Main Phone, Email, Website

Industry/Entity Type

Finance / Lending

Contact Information for Business Card

Logo, Company Name, Company Address, Employee Name, Cell Phone, Main Phone, Email, Website

Requirements
Nice to have
• I'd like the business card to mostly include the logo colors, but a bright color pop of some sort would be nice to see also.

```html
<!DOCTYPE html>
<html lang="en">
<head>
<meta charset="utf-8">
<title>Crestline Lending – Business Card</title>
<link rel="stylesheet" href="https://fonts.googleapis.com/css2?family=Montserrat:wght@400;500;600;700&display=swap">
<style>
  :root {
    --stage: #2b2c2e;
    --paper: #ffffff;
    --navy: #243f86;
    --deep-blue: #264a94;
    --bright-blue: #079fd6;
    --ink: #1b1b1f;
  }
  * { box-sizing: border-box; margin: 0; padding: 0; }
  html, body { width: 1200px; height: 1186px; overflow: hidden; }
  body {
    background: var(--stage);
    font-family: "Montserrat", sans-serif;
    position: relative;
  }
  .card {
    position: absolute;
    left: 150px;
    width: 900px;
    height: 514px;
    border-radius: 36px;
    overflow: hidden;
  }
  .card-back {
    top: 60px;
    background: linear-gradient(200deg, var(--bright-blue) 0%, var(--deep-blue) 100%);
  }
  .back-pattern {
    position: absolute; inset: 0;
    background: linear-gradient(200deg, rgba(255,255,255,0.08), rgba(255,255,255,0.02));
  }
  .back-mark {
    position: absolute;
    right: 70px; top: 200px;
    display: flex; align-items: center; gap: 12px;
    color: var(--paper);
    font-weight: 700; font-size: 24px; letter-spacing: 2px;
  }
  .back-mark .dot { width: 22px; height: 22px; border-radius: 50%; background: var(--paper); }

  .card-front { top: 612px; background: var(--paper); }
  .brand {
    position: absolute; left: 150px; top: 90px;
    display: flex; align-items: center; gap: 14px;
    color: var(--navy);
    font-weight: 700; font-size: 30px; letter-spacing: 3px;
  }
  .brand .dot { width: 30px; height: 30px; border-radius: 50%; background: var(--navy); }
  .band {
    position: absolute; left: 0; right: 0; top: 235px; height: 175px;
    background: linear-gradient(90deg, var(--deep-blue) 0%, #1d6fb6 50%, var(--bright-blue) 100%);
    display: flex; align-items: center;
    color: var(--paper);
  }
  .person { width: 430px; text-align: right; padding-right: 36px; }
  .person-name { font-weight: 700; font-size: 32px; }
  .person-role { font-weight: 400; font-size: 19px; margin-top: 4px; }
  .divider { width: 1.5px; height: 105px; background: rgba(255,255,255,0.6); }
  .contacts { list-style: none; padding-left: 36px; font-size: 18px; line-height: 31px; }
  .contacts li { display: flex; align-items: center; gap: 12px; }
  .contacts svg { width: 16px; height: 16px; fill: var(--paper); flex: none; }
  .address {
    position: absolute; left: 0; right: 0; top: 448px;
    text-align: center; font-size: 19px; color: var(--ink);
  }
</style>
</head>
<body>
  <section class="card card-back" aria-label="Card back">
    <div class="back-pattern" role="img" aria-label="Soft blue field where a repeating brand pattern sits"></div>
    <div class="back-mark"><span class="dot"></span>CRESTLINE</div>
  </section>

  <section class="card card-front" aria-label="Card front">
    <div class="brand"><span class="dot"></span>CRESTLINE LENDING</div>
    <div class="band">
      <div class="person">
        <p class="person-name">Jonah Rellis</p>
        <p class="person-role">CEO &amp; Founder</p>
      </div>
      <div class="divider"></div>
      <ul class="contacts">
        <li><svg viewBox="0 0 16 16"><path d="M3 1h3l1 4-2 1c1 2 3 4 5 5l1-2 4 1v3c0 1-1 2-2 2C7 15 1 9 1 3c0-1 1-2 2-2z"/></svg>877-555-0142</li>
        <li><svg viewBox="0 0 16 16"><path d="M4 0h8a1 1 0 0 1 1 1v14a1 1 0 0 1-1 1H4a1 1 0 0 1-1-1V1a1 1 0 0 1 1-1zm1 2v10h6V2zm3 11a1 1 0 1 0 0 2 1 1 0 0 0 0-2z"/></svg>877-555-0142</li>
        <li><svg viewBox="0 0 16 16"><path d="M0 3h16v1L8 9 0 4zm0 3l8 5 8-5v7H0z"/></svg>info@crestlinelending.com</li>
        <li><svg viewBox="0 0 16 16"><path d="M8 0a8 8 0 1 0 0 16A8 8 0 0 0 8 0zm0 2c1 1 2 3 2 6s-1 5-2 6c-1-1-2-3-2-6s1-5 2-6zM2 8h12v1H2z"/></svg>www.crestlinelending.com</li>
      </ul>
    </div>
    <p class="address">418 Harbor Point Rd, #310 Lakemont, OH 43000</p>
  </section>
</body>
</html>
```